New Zealand Marlborough Sauvignon Blanc wine packaging design

We need packaging design for our new wine brand, Dunmore Hale. The wine is a New Zealand Marlborough Sauvignon Blanc. We would like the packaging will portray elegance and style with an understated label. We are looking for a label that portrays the elegance of the French Riviera. The label should be round or pill shaped.
Updates

Industry/Entity Type

Wine

Font styles to use
Serif
Sans Serif

Requirements
Must have
• The words in order of importance: Dunmore Hale, Sauvignon Blanc, Marlborough, New Zealand. It should be fit to the bottle posted in the links
Nice to have
• a pill shape or circular shape
Should not have
• Illustrations of wine bottles, wine glasses, or grapes

```html
<!DOCTYPE html>
<html lang="en">
<head>
<meta charset="utf-8">
<title>Dunmore Hale Sauvignon Blanc Label</title>
<link rel="stylesheet" href="https://fonts.googleapis.com/css2?family=DM+Serif+Display&family=Playfair+Display:wght@700;800&display=swap">
<style>
  :root {
    --backdrop: #ebebeb;
    --label: #ffffff;
    --leaf-green: #97c11f;
    --ink: #111111;
    --paper-text: #ffffff;
  }
  * { margin: 0; padding: 0; box-sizing: border-box; }
  html, body {
    width: 1200px;
    height: 675px;
    overflow: hidden;
    background: var(--backdrop);
  }
  .canvas {
    position: relative;
    width: 1200px;
    height: 675px;
    background: var(--backdrop);
  }
  .label {
    position: absolute;
    left: 409px;
    top: 57px;
    width: 382px;
    height: 560px;
    background: var(--label);
    border-radius: 191px 191px 191px 191px / 191px 191px 191px 191px;
    overflow: hidden;
  }
  .brand-name {
    position: absolute;
    font-family: "DM Serif Display", serif;
    font-weight: 400;
    color: var(--leaf-green);
    font-size: 69px;
    line-height: 1;
    letter-spacing: -1px;
    white-space: nowrap;
  }
  .brand-name--first { left: 32px; top: 104px; }
  .brand-name--second { left: 45px; top: 158px; }
  .varietal {
    position: absolute;
    font-family: "Playfair Display", serif;
    font-weight: 800;
    color: var(--ink);
    font-size: 22px;
    line-height: 1;
    white-space: nowrap;
  }
  .varietal--grape { left: 45px; top: 217px; }
  .varietal--style { left: 80px; top: 234px; }
  .region-disc {
    position: absolute;
    left: 74px;
    top: 252px;
    width: 308px;
    height: 308px;
    border-radius: 50%;
    background: var(--leaf-green);
  }
  .region-name {
    position: absolute;
    left: 120px;
    top: 388px;
    width: 140px;
    text-align: center;
    font-family: "Playfair Display", serif;
    font-weight: 700;
    color: var(--paper-text);
    font-size: 10.5px;
    line-height: 1.15;
  }
</style>
</head>
<body>
  <main class="canvas">
    <section class="label" aria-label="Dunmore Hale Sauvignon Blanc wine label">
      <div class="region-disc" role="img" aria-label="Map of New Zealand in white on a green circle, showing the North and South Islands"></div>
      <h1>
        <span class="brand-name brand-name--first">Dunmore</span>
        <span class="brand-name brand-name--second">Hale</span>
      </h1>
      <h2>
        <span class="varietal varietal--grape">Sauvignon</span>
        <span class="varietal varietal--style">Blanc</span>
      </h2>
      <p class="region-name">Marlborough,<br>New Zealand</p>
    </section>
  </main>
</body>
</html>
```